Label Design for Saffron Company

We need a label design that is unique for our container. The item inside the container is Saffron, and it is 5g in weigh. We need on the label our logo, the weight and quality. Here is the exactly what we want. We want the background to be black for the label and the design to present royalty, and premium quality.

Premium Quality
Grade A+ Premium Saffron
100% Natural and Pure
www.VarenthaSpice.com

Target Market(s)

Everyone

Requirements
Must have
• Black background, golden border design. Unique design, that show premium and royalty.
Nice to have
• The logo is attached with transparent background so you can show exactly how things look like.
Should not have
• different colors that are not part of the logo.

```html
<!DOCTYPE html>
<html lang="en">
<head>
<meta charset="utf-8">
<title>Varentha Spice – Saffron Tin Label</title>
<link rel="stylesheet" href="https://fonts.googleapis.com/css2?family=Cormorant+Garamond:wght@500;600&family=Crimson+Text:wght@600;700&display=swap">
<style>
  :root {
    --backdrop: #a4a4a4;
    --label-black: #050505;
    --label-charcoal: #1c1c1c;
    --gold-deep: #a87f33;
    --gold-mid: #d6b56a;
    --gold-light: #f3e2a6;
    --saffron-red: #e0180f;
    --ivory: #f2f0ea;
    --ink: #1a1408;
  }
  * { margin: 0; padding: 0; box-sizing: border-box; }
  html, body {
    width: 811px; height: 1200px; overflow: hidden;
    background: var(--backdrop);
  }
  .canvas { position: relative; width: 811px; height: 1200px; }

  .tin-label {
    position: absolute; left: 25px; top: 220px;
    width: 760px; height: 760px; border-radius: 50%;
    overflow: hidden;
    background: radial-gradient(circle at 50% 40%, var(--label-charcoal) 0%, var(--label-black) 70%);
  }
  .label-art { position: absolute; inset: 0; }

  .centered { position: absolute; left: 0; width: 100%; text-align: center; }

  .brand-mark {
    position: absolute; left: 329px; top: 58px;
    width: 102px; height: 102px;
    border: 2px solid var(--gold-mid); border-radius: 12px;
  }
  .brand-name {
    font-family: "Cormorant Garamond", serif; font-weight: 500;
    color: var(--ivory); line-height: 1;
  }
  .brand-name--top { top: 182px; font-size: 24px; letter-spacing: 6px; }
  .brand-name--main { top: 208px; font-size: 38px; letter-spacing: 2px; }

  .gold-text {
    background: linear-gradient(180deg, var(--gold-light) 0%, var(--gold-mid) 45%, var(--gold-deep) 100%);
    -webkit-background-clip: text; background-clip: text;
    color: transparent;
  }
  .headline {
    font-family: "Cormorant Garamond", serif; font-weight: 600;
    font-size: 100px; line-height: 1;
  }
  .headline--premium { top: 268px; letter-spacing: 1px; }
  .headline--quality { top: 392px; letter-spacing: 9px; }

  .grade-line {
    top: 522px;
    font-family: "Crimson Text", serif; font-weight: 700;
    font-size: 33px; line-height: 1;
  }

  .weight-tag {
    top: 613px;
    font-family: "Crimson Text", serif; font-weight: 700;
    font-size: 24px; line-height: 30px; color: var(--gold-light);
  }
  .purity-line {
    top: 660px;
    font-family: "Crimson Text", serif; font-weight: 700;
    font-size: 30px; line-height: 1; color: var(--ink);
  }
  .web-address {
    top: 708px;
    font-family: "Crimson Text", serif; font-weight: 600;
    font-size: 18px; line-height: 1; color: var(--ink);
  }
</style>
</head>
<body>
<main class="canvas">
  <section class="tin-label" aria-label="Saffron tin lid label">
    <svg class="label-art" width="760" height="760" viewBox="0 0 760 760" aria-hidden="true">
      <defs>
        <linearGradient id="goldBand" x1="0" y1="0" x2="1" y2="0">
          <stop offset="0" stop-color="#b38a3c"/>
          <stop offset="0.35" stop-color="#e9d38f"/>
          <stop offset="0.6" stop-color="#f3e2a6"/>
          <stop offset="1" stop-color="#c29a4a"/>
        </linearGradient>
        <linearGradient id="goldRule" x1="0" y1="0" x2="1" y2="0">
          <stop offset="0" stop-color="#d6b56a" stop-opacity="0"/>
          <stop offset="0.2" stop-color="#d6b56a"/>
          <stop offset="0.8" stop-color="#d6b56a"/>
          <stop offset="1" stop-color="#d6b56a" stop-opacity="0"/>
        </linearGradient>
      </defs>

      <line x1="190" y1="512" x2="570" y2="512" stroke="url(#goldRule)" stroke-width="2"/>
      <line x1="190" y1="574" x2="570" y2="574" stroke="url(#goldRule)" stroke-width="1.5"/>

      <path d="M0 604 Q380 618 760 604 L760 760 L0 760 Z" fill="url(#goldBand)"/>
      <ellipse cx="380" cy="628" rx="70" ry="17" fill="#080808" stroke="#8a6a2a" stroke-width="1.5"/>

      <g fill="#e0180f">
        <circle cx="91" cy="223" r="16"/>
        <circle cx="70" cy="268" r="13"/>
        <circle cx="54" cy="322" r="9"/>
        <circle cx="50" cy="376" r="9"/>
        <circle cx="710" cy="372" r="6"/>
        <circle cx="706" cy="405" r="9"/>
        <circle cx="702" cy="442" r="13"/>
        <circle cx="692" cy="491" r="17"/>
      </g>
    </svg>

    <div class="brand-mark" aria-hidden="true"></div>
    <p class="centered brand-name brand-name--top">VARENTHA</p>
    <p class="centered brand-name brand-name--main">SPICE</p>

    <h1 class="centered headline headline--premium gold-text">Premium</h1>
    <p class="centered headline headline--quality gold-text">Quality</p>

    <p class="centered grade-line gold-text">Grade A+ Premium Saffron</p>

    <p class="centered weight-tag">5g</p>
    <p class="centered purity-line">100% Natural and Pure</p>
    <p class="centered web-address">www.VarenthaSpice.com</p>
  </section>
</main>
</body>
</html>
```